Tess Marlowe Communication business card

I am starting a small, country-based business that offers writing, communication and marketing services to a wide range of clients, inner city big business, to mining, through to agriculture.

The appeal of my business is that it's mobile and flexible. It's just me, with lots of hands-on experience on construction and infrastructure projects.

I can provide the following services:

• Communication planning and management
• Issues and media management
• Marketing and communication materials
• Project management and strategy
• Government liaison
• Incident management communication
• Stakeholder management

It would be great to be able to use the elements of the business card design on other stationery.

Industry/Entity Type

Communication

Requirements
Must have
• The following information:

Tess Marlowe
M: 0427 391 864
E: tess@tmcommsmail.com

PO Box 152
Durrandale Q 4472
Nice to have
• a rural element (windmill, workboots, wheat stalk)

```html
<!DOCTYPE html>
<html lang="en">
<head>
<meta charset="utf-8">
<title>Tess Marlowe Communication – Business Cards</title>
<link rel="stylesheet" href="https://fonts.googleapis.com/css2?family=Didact+Gothic&display=swap">
<style>
  :root {
    --backdrop: #2b2b2b;
    --card-black: #050505;
    --card-white: #ffffff;
    --brand-blue: #1d5f86;
    --ink-dark: #1a1a1a;
    --ink-light: #f2f2f2;
    --rule-grey: #9a9a9a;
  }
  * { box-sizing: border-box; margin: 0; padding: 0; }
  html, body {
    width: 1200px;
    height: 900px;
    overflow: hidden;
    background: var(--backdrop);
    font-family: "Didact Gothic", "Century Gothic", sans-serif;
  }
  .stage {
    position: relative;
    width: 1200px;
    height: 900px;
  }
  .card {
    position: absolute;
    left: 270px;
    width: 660px;
    height: 380px;
    overflow: hidden;
    box-shadow: 0 12px 30px rgba(0,0,0,0.55);
  }
  .card--front { top: 50px; }
  .card--reverse { top: 470px; }

  .card__brand {
    position: absolute;
    left: 0; top: 0;
    width: 100%;
    height: 186px;
    display: flex;
    align-items: center;
    padding-left: 120px;
    gap: 22px;
  }
  .card__details {
    position: absolute;
    left: 0; top: 194px;
    width: 100%;
    height: 186px;
  }
  .card__divider {
    position: absolute;
    left: 0; top: 186px;
    width: 100%;
    height: 8px;
  }

  .card--front .card__brand { background: var(--card-black); }
  .card--front .card__details { background: var(--card-white); color: var(--ink-dark); }
  .card--front .card__divider {
    background: linear-gradient(var(--card-black) 0 1px, var(--card-white) 1px 4px, var(--card-black) 4px 6px, var(--card-white) 6px);
  }
  .card--reverse .card__brand { background: var(--card-white); }
  .card--reverse .card__details { background: var(--card-black); color: var(--ink-light); }
  .card--reverse .card__divider {
    background: linear-gradient(var(--card-white) 0 2px, var(--card-black) 2px 4px, var(--card-white) 4px 5px, var(--card-black) 5px);
  }

  .brand-dot {
    width: 64px;
    height: 64px;
    border-radius: 50%;
    background: var(--brand-blue);
    flex: none;
  }
  .brand-name {
    color: var(--brand-blue);
    font-weight: 400;
    line-height: 1;
  }
  .brand-name__main {
    display: block;
    font-size: 52px;
  }
  .brand-name__sub {
    display: block;
    font-size: 19px;
    letter-spacing: 0.32em;
    margin-top: 6px;
    padding-left: 4px;
  }

  .holder {
    position: absolute;
    left: 90px;
    top: 62px;
  }
  .holder__name {
    font-size: 24px;
    letter-spacing: 0.02em;
    text-transform: uppercase;
  }
  .holder__role {
    font-size: 15px;
    text-transform: uppercase;
    margin-top: 2px;
  }
  .details-rule {
    position: absolute;
    left: 330px;
    top: 18px;
    width: 2px;
    height: 140px;
  }
  .card--front .details-rule {
    background: linear-gradient(transparent, var(--ink-dark) 55%, transparent);
  }
  .card--reverse .details-rule {
    background: linear-gradient(transparent, var(--ink-light) 55%, transparent);
  }
  .contact {
    position: absolute;
    left: 370px;
    top: 30px;
    font-size: 14px;
    line-height: 1.35;
    font-style: normal;
  }
  .contact__lines { margin-top: 14px; }
  .contact__lines p + p { margin-top: 8px; }
</style>
</head>
<body>
<main class="stage">

  <section class="card card--front" aria-label="Business card, dark header">
    <header class="card__brand">
      <span class="brand-dot"></span>
      <h1 class="brand-name">
        <span class="brand-name__main">Tess Marlowe</span>
        <span class="brand-name__sub">COMMUNICATION</span>
      </h1>
    </header>
    <div class="card__divider"></div>
    <div class="card__details">
      <div class="holder">
        <p class="holder__name">Tess Marlowe</p>
        <p class="holder__role">Position</p>
      </div>
      <div class="details-rule"></div>
      <address class="contact">
        <p>PO Box 152<br>Durrandale Q 4472</p>
        <div class="contact__lines">
          <p>M: 0427 391 864</p>
          <p>E: tess@tmcommsmail.com</p>
        </div>
      </address>
    </div>
  </section>

  <section class="card card--reverse" aria-label="Business card, light header">
    <header class="card__brand">
      <span class="brand-dot"></span>
      <h2 class="brand-name">
        <span class="brand-name__main">Tess Marlowe</span>
        <span class="brand-name__sub">COMMUNICATION</span>
      </h2>
    </header>
    <div class="card__divider"></div>
    <div class="card__details">
      <div class="holder">
        <p class="holder__name">Tess Marlowe</p>
        <p class="holder__role">Position</p>
      </div>
      <div class="details-rule"></div>
      <address class="contact">
        <p>PO Box 152<br>Durrandale Q 4472</p>
        <div class="contact__lines">
          <p>M: 0427 391 864</p>
          <p>E: tess@tmcommsmail.com</p>
        </div>
      </address>
    </div>
  </section>

</main>
</body>
</html>
```